label redesign for skincare product

We would like a redesign of existing labels for a skincare product that we make (the existing labels are attached). This is a very natural product, but the existing labels are not right - one of the labels wraps around the jar, and one of the labels is placed on the bottom of the jar (copies of these attached). It needs softening and to be made less brutal looking. The label needs to communicate luxury quality product, that contains natural products, whilst maintaining a contemporary feel. The audience is male and female.

The product is called 'Dew Haven' and our company is called RB Naturals. We have a website at www.rbnaturals-example.com where the existing product can be seen. It is NOT however necessary for the RB Naturals logo from the website to be used on the label - this is at the discretion of the designer.

The packaging will remain the same - this is a glass jar in extremely deep purple, almost black.

The colour of the product inside the jar is off white. The product contain mandarin and geranium essential oils so is floral and citrussy smelling.

Target Market(s)

Adults who like high quality natural skincare products, 30-65.

Industry/Entity Type

It Company

Font styles to use
Serif
Sans Serif

Colors

Designer to choose colors to be used in the design.

Requirements
Must have
• The long label must by 13mm high and 110 mm wide. The round label for the back of the jar must be 40mm diameter..

```html
<!DOCTYPE html>
<html lang="en">
<head>
<meta charset="utf-8">
<title>Dew Haven – jar label options</title>
<link rel="stylesheet" href="https://fonts.googleapis.com/css2?family=Marcellus&family=PT+Sans:wght@400;700&display=swap">
<style>
  :root {
    --plum: #5b1a68;
    --orange: #f6a444;
    --orange-deep: #f39a3a;
    --peach: #fcd9b6;
    --peach-light: #fde9d5;
    --cream: #fff7ef;
    --white: #ffffff;
    --bg-top: #ffffff;
    --bg-bottom: #fbdec0;
  }
  * { margin: 0; padding: 0; box-sizing: border-box; }
  html, body { width: 780px; height: 1200px; overflow: hidden; }
  body {
    position: relative;
    background: linear-gradient(to bottom, var(--bg-top) 15%, var(--bg-bottom) 100%);
    font-family: "PT Sans", sans-serif;
  }
  .label {
    position: absolute;
    left: 50px;
    width: 680px;
    height: 84px;
    border-radius: 8px;
    overflow: hidden;
    display: flex;
    box-shadow: 0 2px 6px rgba(91, 26, 104, 0.12);
  }
  .label--one { top: 190px; }
  .label--two { top: 558px; }
  .label--three { top: 926px; }

  .name-panel {
    position: relative;
    width: 500px;
    height: 100%;
    display: flex;
    align-items: center;
    padding-left: 24px;
  }
  .label--one .name-panel {
    background:
      linear-gradient(to bottom,
        transparent 0 6px, var(--orange) 6px 8px, transparent 8px 12px,
        var(--white) 12px 14px, transparent 14px 70px,
        var(--white) 70px 72px, transparent 72px 76px,
        var(--orange) 76px 78px, transparent 78px),
      linear-gradient(to right, var(--white) 0%, var(--white) 18%, var(--peach-light) 45%, var(--peach) 75%, var(--orange) 100%);
  }
  .label--two .name-panel {
    background:
      linear-gradient(to bottom,
        transparent 0 5px, var(--orange) 5px 7px, transparent 7px 10px,
        var(--white) 10px 14px, transparent 14px 70px,
        var(--white) 70px 74px, transparent 74px 77px,
        var(--orange) 77px 79px, transparent 79px),
      linear-gradient(to right, var(--white) 0%, var(--white) 22%, var(--peach-light) 50%, var(--peach) 78%, var(--orange) 100%);
  }
  .pattern-field {
    position: absolute;
    inset: 0;
    background: linear-gradient(to right, var(--orange) 0%, var(--peach) 20%, var(--orange-deep) 45%, var(--peach-light) 70%, var(--peach) 100%);
  }
  .product-name {
    position: relative;
    font-family: "Marcellus", serif;
    font-size: 60px;
    line-height: 1;
    letter-spacing: 1px;
    color: var(--plum);
    white-space: nowrap;
  }

  .info-panel {
    width: 180px;
    height: 100%;
    padding: 9px 10px 6px 12px;
    background: var(--orange);
    color: var(--plum);
    font-size: 9px;
    line-height: 11px;
  }
  .label--three .info-panel { background: var(--peach); }
  .info-title { font-weight: 700; }
</style>
</head>
<body>

  <div class="label label--one">
    <div class="name-panel">
      <span class="product-name">DEW HAVEN</span>
    </div>
    <div class="info-panel">
      <p class="info-title">RB Naturals Dew Haven</p>
      <p>Moisturising salve for dry skin that needs some love. Keep out of reach of children. Test on a patch of skin first. Stop use if irritation occurs. RB Naturals, 14 Willow Lane</p>
    </div>
  </div>

  <div class="label label--two">
    <div class="name-panel">
      <span class="product-name">DEW HAVEN</span>
    </div>
    <div class="info-panel">
      <p class="info-title">RB Naturals Dew Haven</p>
      <p>Moisturising salve for dry skin that needs some love. Keep out of reach of children. Test on a patch of skin first. Stop use if irritation occurs. RB Naturals, 14 Willow Lane</p>
    </div>
  </div>

  <div class="label label--three">
    <div class="name-panel">
      <div class="pattern-field" role="img" aria-label="Checkered pattern of orange, peach and cream squares"></div>
      <span class="product-name">DEW HAVEN</span>
    </div>
    <div class="info-panel">
      <p class="info-title">RB Naturals Dew Haven</p>
      <p>Moisturising salve for dry skin that needs some love. Keep out of reach of children. Test on a patch of skin first. Stop use if irritation occurs. RB Naturals, 14 Willow Lane</p>
    </div>
  </div>

</body>
</html>
```